Belarde's Plumbing, Heating, and AC Buisness card

I need a business card design for my Plumbing Heating and AC company. We are based out of North Windham, CT, and offer residential and light commercial services. I am looking for something that incorporates a water droplet, snowflake, and flame. I would like it to be Modern and different from a typical business card but needs to communicate confidence and security.

```html
<!DOCTYPE html>
<html lang="en">
<head>
<meta charset="utf-8">
<title>Belarde's Plumbing, Heating, and AC – Business Card</title>
<link href="https://fonts.googleapis.com/css2?family=Exo+2:wght@400;500;700;800&display=swap" rel="stylesheet">
<style>
  :root {
    --bg: #e9e6e1;
    --card: #000000;
    --ink: #ffffff;
    --brand-blue: #4f8fd8;
    --icon-blue: #8fb4e6;
    --water: #1e74c9;
    --water-deep: #0a3d7a;
    --flame: #ff8a1c;
    --flame-deep: #d8361a;
  }
  * { margin: 0; padding: 0; box-sizing: border-box; }
  html, body {
    width: 1200px; height: 779px; overflow: hidden;
    background: var(--bg);
    font-family: "Exo 2", sans-serif;
  }
  .canvas { position: relative; width: 1200px; height: 779px; }
  .card {
    position: absolute; top: 204px;
    width: 509px; height: 328px;
    background: var(--card);
    overflow: hidden;
    box-shadow: 2px 3px 6px rgba(0,0,0,.35);
    color: var(--ink);
  }
  .card--front { left: 69px; }
  .card--back { left: 613px; top: 201px; }

  /* soft glows: every gradient fades to transparent inside its own box */
  .art { position: absolute; }
  .art--flame {
    background: radial-gradient(closest-side, #ffd23a 0%, var(--flame) 35%, var(--flame-deep) 62%, rgba(216,54,26,.35) 80%, rgba(0,0,0,0) 100%);
  }
  .art--water {
    background: radial-gradient(closest-side, #4fb0ff 0%, var(--water) 35%, var(--water-deep) 65%, rgba(10,61,122,.3) 85%, rgba(0,0,0,0) 100%);
  }
  .art--ice {
    background: radial-gradient(closest-side, rgba(215,222,230,.6) 0%, rgba(140,150,160,.3) 45%, rgba(0,0,0,0) 100%);
  }

  .front__flame { left: 400px; top: 10px; width: 190px; height: 190px; }
  .front__water { left: 280px; top: 170px; width: 330px; height: 300px; }
  .front__ice { left: 290px; top: 220px; width: 140px; height: 130px; }

  .brand {
    position: absolute; left: 46px; top: 56px;
    display: flex; align-items: flex-start; gap: 30px;
    color: var(--brand-blue);
    font-weight: 800; text-transform: uppercase;
    line-height: 1; font-size: 36px; letter-spacing: 1px;
  }
  .brand__mark { width: 14px; height: 14px; background: var(--brand-blue); margin-top: 10px; }

  .person { position: absolute; left: 92px; top: 182px; }
  .person__name { font-size: 19px; font-weight: 700; margin-bottom: 14px; }
  .contact { display: flex; align-items: center; gap: 14px; font-size: 18px; font-weight: 500; letter-spacing: .3px; margin-bottom: 10px; }
  .contact svg { width: 20px; height: 20px; flex: none; }

  .back__ice { left: -90px; top: -90px; width: 300px; height: 280px; }
  .back__flame { left: 320px; top: -70px; width: 240px; height: 260px; }
  .back__water { left: -60px; top: 190px; width: 630px; height: 280px; }

  .web-icon { position: absolute; left: 216px; top: 86px; width: 76px; height: 76px; }
  .web-url {
    position: absolute; left: 0; right: 0; top: 175px;
    text-align: center; font-size: 24px; font-weight: 500; letter-spacing: .4px;
  }
</style>
</head>
<body>
<main class="canvas">

  <section class="card card--front">
    <div class="art art--water front__water" role="img" aria-label="Photograph of blue water with a falling droplet"></div>
    <div class="art art--flame front__flame" role="img" aria-label="Photograph of an orange flame"></div>
    <div class="art art--ice front__ice" role="img" aria-label="Photograph of an ice snowflake"></div>

    <div class="brand">
      <span class="brand__mark"></span>
      <span>Belarde's<br>Plumbing</span>
    </div>

    <div class="person">
      <p class="person__name">Name Surname</p>
      <p class="contact">
        <svg viewBox="0 0 20 20" fill="none" stroke="var(--icon-blue)" stroke-width="1.6"><rect x="1.5" y="4" width="17" height="12"/><path d="M1.5 4l8.5 7 8.5-7M1.5 16l6-6M18.5 16l-6-6"/></svg>
        email@email.com
      </p>
      <p class="contact">
        <svg viewBox="0 0 20 20" fill="var(--icon-blue)"><rect x="5" y="1" width="10" height="18" rx="2.5"/><rect x="7" y="4" width="6" height="6" fill="#000"/></svg>
        123456789
      </p>
    </div>
  </section>

  <section class="card card--back">
    <div class="art art--water back__water" role="img" aria-label="Photograph of blue water with falling droplets"></div>
    <div class="art art--ice back__ice" role="img" aria-label="Photograph of an ice snowflake"></div>
    <div class="art art--flame back__flame" role="img" aria-label="Photograph of an orange flame"></div>

    <svg class="web-icon" viewBox="0 0 76 76" fill="none" stroke="var(--icon-blue)" stroke-width="6">
      <circle cx="36" cy="36" r="31"/>
      <ellipse cx="36" cy="36" rx="13" ry="31"/>
      <path d="M5 28h62M5 44h40"/>
      <path d="M48 42l22 12-9 3 7 11-5 3-7-11-6 6z" fill="var(--icon-blue)" stroke="#000" stroke-width="2"/>
    </svg>
    <p class="web-url">www.BelardesPlumbing.com</p>
  </section>

</main>
</body>
</html>
```